I need a new business card design for my pharmacy.

I need a business card design. I will include my logo.
The card needs to be readable. I prefer to have my logo on one side along with my website, the other side includes the other information. Please use combination of black, neon green, white, and silver. This needs to catch the eye but yet be clearly visible and legible. Thanks

Industry/Entity Type

Pharmacy

Contact Information for Business Card

It needs to have the following information listed:
Mel's Apothecary Owner/Pharm D.
7134 North Brook Lane
Sioux Falls, SD 57231
Phone 605-318-6207
Fax 605-318-6209
email: mel@melsapothecary-example.com
www.melsapothecary-example.com
Store hours Monday-Friday 8 am- 7 pm
Saturday 8 am- 12 pm
Sunday Closed
Please utilize the colors black, white, and neon green, maybe silver.

Requirements
Must have
• It needs to be easily readable!
Nice to have
• It should catch the eye.
Should not have
• Do not use any other colors except listed: black, neon green, white, & silver.

```html
<!DOCTYPE html>
<html lang="en">
<head>
<meta charset="utf-8">
<title>Mel's Apothecary – Business Card</title>
<link rel="stylesheet" href="https://fonts.googleapis.com/css2?family=Encode+Sans+Condensed:wght@600&family=Open+Sans:wght@400&display=swap">
<style>
  :root {
    --paper: #ffffff;
    --ink: #1d1d1b;
    --green-deep: #4f9a22;
    --green: #7cc242;
    --green-bright: #8fd14f;
    --green-light: #c6e6a3;
    --green-pale: #eaf6dd;
  }
  * { margin: 0; padding: 0; box-sizing: border-box; }
  html, body {
    width: 1200px; height: 417px; overflow: hidden;
    background: var(--paper);
  }
  .canvas { position: relative; width: 1200px; height: 417px; }
  .card {
    position: absolute; top: 52px; width: 562px; height: 312px;
    overflow: hidden;
  }
  .card--front { left: 14px; background: var(--paper); }
  .card--back { left: 612px; }

  .card__backdrop { position: absolute; inset: 0; }
  .card--front .card__backdrop {
    background: linear-gradient(to bottom,
      var(--paper) 0%, var(--paper) 30%,
      var(--green-pale) 50%, var(--green-light) 72%, var(--green) 100%);
  }
  .card--back .card__backdrop {
    background: linear-gradient(to bottom,
      var(--green-deep) 0%, var(--green) 35%, var(--green-bright) 52%,
      var(--green-pale) 72%, var(--green-light) 100%);
  }

  .brand {
    position: absolute; display: flex; align-items: center;
    font-family: "Encode Sans Condensed", "Arial Narrow", sans-serif;
    font-weight: 600; color: var(--ink); letter-spacing: -0.3px;
    white-space: nowrap;
  }
  .brand__dot { border-radius: 50%; background: var(--ink); flex: none; }
  .brand--front { right: 24px; top: 70px; font-size: 31px; gap: 14px; }
  .brand--front .brand__dot { width: 26px; height: 26px; }
  .brand--back { left: 40px; top: 140px; font-size: 20px; gap: 10px; }
  .brand--back .brand__dot { width: 18px; height: 18px; }

  .role {
    position: absolute; left: 68px; top: 170px;
    font-family: "Open Sans", Arial, sans-serif; font-size: 12px; color: var(--ink);
  }

  .website {
    position: absolute; right: 24px; top: 115px;
    font-family: "Open Sans", Arial, sans-serif; font-size: 14px; color: var(--ink);
  }

  .contact {
    position: absolute; left: 283px; top: 64px; list-style: none;
    font-family: "Open Sans", Arial, sans-serif; font-size: 12.5px;
    line-height: 15px; color: var(--ink);
  }
  .contact__item { display: flex; gap: 8px; align-items: flex-start; }
  .contact__item + .contact__item { margin-top: 19px; }
  .contact__item--hours { margin-top: 14px !important; }
  .contact__icon { width: 16px; height: 16px; flex: none; fill: var(--ink); margin-top: 1px; }
  .contact__icon--hours { margin-top: 7px; }
</style>
</head>
<body>
<main class="canvas">

  <section class="card card--front" aria-label="Card front">
    <div class="card__backdrop" role="img" aria-label="Flowing green wave pattern across the lower card"></div>
    <div class="brand brand--front"><span class="brand__dot"></span><span class="brand__name">Mel's Apothecary</span></div>
    <p class="website">www.melsapothecary-example.com</p>
  </section>

  <section class="card card--back" aria-label="Card back">
    <div class="card__backdrop" role="img" aria-label="Green background with flowing wave pattern"></div>

    <div class="brand brand--back"><span class="brand__dot"></span><span class="brand__name">Mel's Apothecary</span></div>
    <p class="role">Owner/Pharm D.</p>

    <ul class="contact">
      <li class="contact__item">
        <svg class="contact__icon" viewBox="0 0 16 16" aria-hidden="true"><path d="M8 0a5.5 5.5 0 0 0-5.5 5.5C2.5 10 8 16 8 16s5.5-6 5.5-10.5A5.5 5.5 0 0 0 8 0zm0 8a2.5 2.5 0 1 1 0-5 2.5 2.5 0 0 1 0 5z"/></svg>
        <span>7134 North Brook Lane<br>Sioux Falls, SD 57231</span>
      </li>
      <li class="contact__item contact__item--hours">
        <svg class="contact__icon contact__icon--hours" viewBox="0 0 16 16" aria-hidden="true"><path d="M8 0l-4 5h1.5L8 2l2.5 3H12L8 0zM0 5h16v10H0z"/></svg>
        <span>Store hours Monday-Friday 8 am- 7 pm<br>Saturday 8 am- 12 pm<br>Sunday Closed</span>
      </li>
      <li class="contact__item">
        <svg class="contact__icon" viewBox="0 0 16 16" aria-hidden="true"><path d="M3.6 0.5l2.4 3.2-1.5 2a9 9 0 0 0 5.8 5.8l2-1.5 3.2 2.4-1.3 2.6C9 16 0 7 0.9 1.8z"/></svg>
        <span>605-318-6207</span>
      </li>
      <li class="contact__item">
        <svg class="contact__icon" viewBox="0 0 16 16" aria-hidden="true"><path d="M4 0h8v4H4zM0 5h16v11H0zm3 3v2h10V8zm0 4v1h3v-1zm5 0v1h5v-1z"/></svg>
        <span>605-318-6209</span>
      </li>
      <li class="contact__item">
        <svg class="contact__icon" viewBox="0 0 16 16" aria-hidden="true"><path d="M0 3h16v1.2L8 9 0 4.2zM0 6l8 4.8L16 6v8H0z"/></svg>
        <span>mel@melsapothecary-example.com</span>
      </li>
    </ul>
  </section>

</main>
</body>
</html>
```